*YO!!! Designers Needed!!* Front Page Cover Needed for a $$Billion Dollar$$ Company

We are a manufacturer of aluminum electrolytic capacitors. We are looking to create a front page cover that will be used on our annual report. We are a publicly listed company and work with many Pinnacle 300 companies, so your work will be viewed by the BIG GUNS and EXECUTIVES around the WORLD! If selected, you may be selected for additional work.

The front page cover should be unique. If elegance, modern, bling, and creativity somehow got together and had a child, that's what the cover page would look like!

Inspired Examples attached. Check them out!

www.velmoro.com

Font styles to use
Sans Serif

Requirements
Must have
• 1. Must include the attached logo. Logo size, color, and placement are at your discretion.

2. Should include the text, '2020 Annual Report'

3. The design should incorporate the use of foil and/or be embossed. The foil can be part of the design or can be the full page. See various examples attached for reference.

4. Shall be in A4 size and vertical orientation.
Nice to have
• Feel free to add any icons or stock photos (for example capacitors or circuit boards) if needed.

Be creative here and don't be afraid to be bold! The end product will be printed and budget is not a limiting factor, so feel free to make it extravagant if needed.

Our slogan is "Think Ahead". This slogan can or cannot be part of the theme.

```html
<!DOCTYPE html>
<html lang="en">
<head>
<meta charset="UTF-8">
<title>Velmoro 2020 Annual Report Cover</title>
<link rel="stylesheet" href="https://fonts.googleapis.com/css2?family=Oswald:wght@400;600;700&display=swap">
<style>
  :root {
    --backdrop: #76a3a5;
    --paper: #f1f1f1;
    --paper-shade: #e9e9e9;
    --navy: #1b2e63;
    --mint-frame: #a5cfc4;
    --sage-band: #85aeaa;
    --lavender-edge: #b9b7c8;
    --foil-light: #3cc6ac;
    --foil-mid: #1fa78d;
    --foil-dark: #15826e;
  }
  * { margin: 0; padding: 0; box-sizing: border-box; }
  html, body {
    width: 1200px;
    height: 900px;
    overflow: hidden;
    background: var(--backdrop);
  }
  .canvas {
    position: relative;
    width: 1200px;
    height: 900px;
  }
  .cover {
    position: absolute;
    left: 310px;
    top: 40px;
    width: 580px;
    height: 820px;
    background: linear-gradient(170deg, var(--paper) 0%, var(--paper-shade) 100%);
    box-shadow: 0 18px 40px rgba(0, 0, 0, 0.18);
    overflow: hidden;
  }
  .brand {
    position: absolute;
    right: 78px;
    top: 96px;
    display: flex;
    align-items: center;
    gap: 8px;
    font-family: "Oswald", sans-serif;
    font-weight: 700;
    font-size: 34px;
    letter-spacing: 1px;
    color: var(--navy);
  }
  .brand-mark {
    width: 12px;
    height: 12px;
    background: var(--navy);
  }
  .emblem {
    position: absolute;
    left: 0;
    top: 0;
    width: 580px;
    height: 820px;
  }
  .title {
    position: absolute;
    right: 62px;
    top: 560px;
    text-align: right;
    font-family: "Oswald", sans-serif;
    color: var(--navy);
    line-height: 1;
  }
  .title-year {
    display: block;
    font-weight: 700;
    font-size: 78px;
    letter-spacing: 3px;
  }
  .title-label {
    display: block;
    margin-top: 12px;
    font-weight: 400;
    font-size: 50px;
    letter-spacing: 3px;
  }
</style>
</head>
<body>
  <main class="canvas">
    <section class="cover">
      <div class="brand">
        <span class="brand-mark"></span>
        <span class="brand-name">VELMORO</span>
      </div>

      <svg class="emblem" viewBox="0 0 580 820" xmlns="http://www.w3.org/2000/svg">
        <defs>
          <linearGradient id="foil-fill" x1="0" y1="0" x2="1" y2="1">
            <stop offset="0" stop-color="var(--foil-mid)"/>
            <stop offset="0.45" stop-color="var(--foil-light)"/>
            <stop offset="0.75" stop-color="var(--foil-dark)"/>
            <stop offset="1" stop-color="var(--foil-mid)"/>
          </linearGradient>
        </defs>
        <polygon class="emblem-edge" points="88,326 420,336 186,628" fill="var(--lavender-edge)"/>
        <polygon class="emblem-frame" points="98,318 446,328 198,622" fill="var(--mint-frame)"/>
        <polygon class="emblem-band" points="110,328 428,336 200,604" fill="var(--sage-band)"/>
        <polygon class="emblem-foil" points="140,344 396,350 214,566" fill="url(#foil-fill)"
                 role="img" aria-label="Foil-stamped pattern of small teal and white triangles"/>
      </svg>

      <h1 class="title">
        <span class="title-year">2020</span>
        <span class="title-label">ANNUAL REPORT</span>
      </h1>
    </section>
  </main>
</body>
</html>
```